Sweet website for Wrenfield Flowers

Our name is Wrenfield and we are looking for someone to design a SWEET looking website for us. We would like a site that has a responsive design, clean interface, easy to navigate and smooth user experience. It will be hosted on wordpress and is an ecommerce site so it needs to be fully compatible so that updates can be made easily on the back end.

It is important to us that the design is premium looking, beautiful to look at and has an elegance to it that befits the beautiful products we sell. We don't want it to look like a standard wordpress template so please feel free to be creative.

We have defined basic template pages in wireframes which are NOT by any means a design mandate. Please use this as a guide for what content should be considered in the design on each page. THERE ARE TWO HOMEPAGE OPTIONS (1 has additional content areas - please propose designs for both options) We DO NOT want to see creative that looks exactly like our wireframes. Please come up with fresh creative ideas. (see wireframe doc attached). We have also attached the copy deck, logos, design references to help you to better understand what our customers like.

THANK YOU! LOOKING FORWARD TO SEEING YOUR PROPOSALS!!!
Updates

An updated content/wireframe document has been uploaded. We have 2 content options for the homepage - please propose designs for both layouts.

We have also added a powerpoint with websites that we like so that you can get a better idea of what we would like our website to look like.

Project Deadline Extended
Reason: We are extending the deadline and have increased and guaranteed the payment since we can see potential in the submitted designs but feel that they are currently not at their creative potential. The extra time given should allow for more time to submit original designs that do not look exactly like the wireframes provided.

Target Market(s)

Premium, affluent market

Font styles to use
Sans Serif

Requirements
Must have
• see wireframe, copy and design reference attachments and use as guidelines. The powerpoint presentation shows key areas that we think will be good in our design. Please review them. There are 2 homepage content options. Please propose options for both.
Please take note that option 2 has 3 additional content areas labelled "hand tied bouquets shop now", "Hatbox arrangements shop now" "floral cupcakes shop now" please propose 1 design with this the additional sections and 1 design without.

```html
<!DOCTYPE html>
<html lang="en">
<head>
<meta charset="utf-8">
<title>Wrenfield Flowers</title>
<link href="https://fonts.googleapis.com/css2?family=Questrial&family=Open+Sans:wght@400;600;700&family=Comfortaa:wght@400&display=swap" rel="stylesheet">
<style>
:root{
  --pink:#e8457a;
  --pink-deep:#c2185b;
  --crimson:#a3123f;
  --crimson-dark:#7c0d30;
  --green:#4e7a3a;
  --green-dark:#2f5a22;
  --ink:#3a3a3a;
  --grey:#6b6b6b;
  --grey-dark:#4d4d4d;
  --card:#f6f6f7;
  --white:#ffffff;
}
*{margin:0;padding:0;box-sizing:border-box}
html,body{width:939px;height:1200px;overflow:hidden}
body{
  position:relative;
  font-family:"Questrial",sans-serif;color:var(--ink);
  background:
    radial-gradient(ellipse 300px 260px at 60px 420px,#f7c9d9 0%,rgba(247,201,217,0) 100%),
    radial-gradient(ellipse 260px 300px at 910px 600px,#f9d3df 0%,rgba(249,211,223,0) 100%),
    radial-gradient(ellipse 420px 200px at 470px 840px,#fbd6e2 0%,rgba(251,214,226,0) 100%),
    linear-gradient(180deg,#fdf4f7 0%,#fae3eb 50%,#fcecf1 100%);
}
.abs{position:absolute}

/* top bar */
.topbar{left:0;top:0;width:939px;height:29px;background:linear-gradient(#8a8a8a,#5e5e5e)}
.account-tab{top:6px;height:18px;padding:0 8px;font-size:9px;line-height:18px;color:#eee;
  background:linear-gradient(#6e6e6e,#4e4e4e);border-radius:3px 3px 0 0}
.social-note{right:69px;top:8px;font-size:8.5px;color:#f1f1f1;display:flex;align-items:center;gap:3px}
.social-note .sq{width:11px;height:11px;background:#d9d9d9;border-radius:2px;display:inline-block}

/* header */
.brand{left:78px;top:0;width:198px;height:123px;background:var(--white);box-shadow:0 2px 6px rgba(0,0,0,.18);
  display:flex;flex-direction:column;align-items:center;justify-content:center;gap:8px;text-align:center}
.brand .dot{width:26px;height:26px;border-radius:50%;background:var(--pink)}
.brand .name{font-size:15px;line-height:17px;letter-spacing:3px;color:var(--pink-deep);text-transform:uppercase}
.tagline{left:288px;top:52px;font-family:"Comfortaa",sans-serif;font-size:16px;line-height:21px;color:var(--pink);
  letter-spacing:.5px;text-transform:uppercase;white-space:nowrap}
.vrule{width:1px;background:#e5b8c7}
.hush{left:488px;top:36px;width:205px;font-size:8.4px;line-height:10.6px;color:#333}
.hush b{font-weight:400;text-transform:uppercase}
.hush .field{position:absolute;left:0;top:49px;width:127px;height:13px;background:#fff;border:1px solid #ddd;
  font-size:7px;line-height:11px;padding-left:4px;color:#555}
.hush .signup{position:absolute;left:128px;top:49px;width:39px;height:13px;border-radius:2px;
  background:linear-gradient(#8a8a8a,#5d5d5d);color:#fff;font-size:7.5px;line-height:13px;text-align:center}
.hush .secret{position:absolute;left:0;top:66px;font-size:12px;color:var(--pink);white-space:nowrap}
.contact{left:717px;top:50px;font-size:10.5px;line-height:13.5px;color:#555}
.contact strong{font-family:"Open Sans",sans-serif;font-weight:700;color:#555}
.dotrule{left:276px;top:122px;width:596px;border-top:1px dashed #e8a5bb}

/* nav */
.nav{left:67px;top:138px;width:805px;height:33px;border-radius:3px;
  background:linear-gradient(#c4264f,#a3123f);display:flex;align-items:stretch}
.nav a{color:#fff;text-decoration:none;font-size:9.4px;font-family:"Open Sans",sans-serif;text-transform:uppercase;
  display:flex;align-items:center;padding:0 9px;border-right:1px solid rgba(0,0,0,.2)}
.nav a.active{background:var(--crimson-dark);padding:0 12px}
.nav .search{position:absolute;left:639px;top:9px;width:113px;height:15px;background:#fff;border:1px solid #ddd}
.nav .go{position:absolute;left:752px;top:9px;width:41px;height:15px;background:linear-gradient(#5d5d5d,#3d3d3d);
  color:#fff;font-size:8px;line-height:15px;text-align:center}

/* hero */
.hero{left:67px;top:179px;width:805px;height:340px;background:linear-gradient(90deg,#fafafa,#ececee);
  box-shadow:0 2px 6px rgba(0,0,0,.12);overflow:hidden}
.hero-photo{left:303px;top:0;width:502px;height:340px;
  background:radial-gradient(ellipse 200px 170px at 260px 170px,#f29a3a 0%,#e2477f 45%,#9bc04a 70%,rgba(230,230,232,0) 100%)}
.hero-kicker{left:37px;top:55px;font-size:29px;color:var(--green);text-transform:uppercase;letter-spacing:.5px}
.hero-title{left:37px;top:82px;font-family:"Open Sans",sans-serif;font-weight:700;font-size:32px;color:var(--pink);text-transform:uppercase}
.hero-copy{left:37px;top:127px;width:230px;font-size:10.5px;line-height:12px;color:#333}
.btn-shop{left:37px;top:235px;width:71px;height:17px;border-radius:4px;background:linear-gradient(var(--green),var(--green-dark));
  color:#fff;font-size:8.5px;line-height:17px;text-align:center;text-transform:uppercase}
.dots{left:37px;top:304px;display:flex;gap:4px}
.dots i{width:7px;height:7px;border-radius:50%;background:#777;display:block}
.dots i.on{background:var(--crimson)}
.arrow{top:298px;width:26px;height:25px;background:var(--crimson-dark);display:flex;align-items:center;justify-content:center}

/* cards */
.card{top:541px;height:284px;background:var(--card);box-shadow:0 1px 4px rgba(0,0,0,.2)}
.card h2{height:49px;background:linear-gradient(#e8457a,#b8153f);color:#fff;font-family:"Open Sans",sans-serif;font-weight:700;
  font-size:11.6px;line-height:14px;text-transform:uppercase;padding:0 9px;display:flex;align-items:center}
.card .photo{margin:7px 9px 0;height:124px;border:3px solid #9d9d9d}
.card p{margin:12px 9px 0;font-size:9.8px;line-height:12px;color:#333}

/* featured */
.featured{left:67px;top:854px;width:805px;height:204px;background:#fff;border:1px solid #ddd}
.featured h2{position:absolute;left:10px;top:10px;font-family:"Open Sans",sans-serif;font-weight:700;font-size:16px;color:var(--pink);text-transform:uppercase}
.prod{top:36px;width:160px;height:160px}
.prod .photo{position:absolute;left:20px;top:0;width:125px;height:130px;border-radius:40%}
.prod .price{position:absolute;left:15px;top:92px;width:45px;height:45px;border-radius:50%;background:var(--crimson);
  color:#fff;font-family:"Open Sans",sans-serif;font-weight:700;font-size:9.5px;line-height:10px;text-align:center;padding-top:11px}
.prod .name{position:absolute;left:0;top:145px;width:160px;text-align:center;font-size:10.5px;color:#222}
.sep{top:45px;width:1px;height:145px;background:#ddd}
.chev{top:100px}

/* footer */
.footer{left:67px;top:1085px;width:805px;height:115px;border-top:5px solid var(--pink);background:linear-gradient(#8c8c8c,#5a5a5a);color:#fff}
.footer h3{position:absolute;left:24px;top:17px;font-family:"Open Sans",sans-serif;font-weight:600;font-size:14.5px;text-transform:uppercase}
.footer .line{position:absolute;left:24px;font-size:10px;display:flex;align-items:center;gap:4px}
.footer .sq{width:14px;height:14px;background:#cfcfcf;border-radius:2px;display:inline-block}
.footer .vr{position:absolute;top:17px;width:1px;height:80px;background:rgba(255,255,255,.25)}
.footer .copy{position:absolute;left:208px;top:43px;font-size:8.8px;line-height:15.5px}
.footer .links{position:absolute;left:408px;top:52px;font-size:8.8px}
</style>
</head>
<body>

<div class="abs topbar"></div>
<div class="abs account-tab" style="left:291px">My Account</div>
<div class="abs account-tab" style="left:360px">My Flower Basket</div>
<div class="abs social-note">Like us on <span class="sq"></span> Follow us on <span class="sq"></span> and <span class="sq"></span> for special offers!</div>

<header>
  <div class="abs brand"><span class="dot"></span><span class="name">Wrenfield<br>Flowers</span></div>
  <div class="abs tagline">When words<br>are not enough</div>
  <div class="abs vrule" style="left:473px;top:35px;height:80px"></div>
  <div class="abs hush">
    <b>Can you keep a secret?</b><br>
    Join the Petal Circle and get exclusive member only sales and delivery discounts when you sign up for the Petal Post newsletter!
    <div class="field">Enter your email...</div>
    <div class="signup">Sign up</div>
    <div class="secret">We won't tell if you don't tell!</div>
  </div>
  <div class="abs vrule" style="left:700px;top:35px;height:80px"></div>
  <div class="abs contact">Contact us on:<br><strong>+971500000412</strong><br>or Email us:<br><strong>info@wrenfieldflowers.com</strong></div>
  <div class="abs dotrule"></div>
</header>

<nav class="abs nav">
  <a class="active">Buy Flowers</a><a>Season's Collection</a><a>Weddings &amp; Contracts</a><a>Gifts &amp; Accessories</a><a>Free Updates</a><a style="border:none">Blogs</a>
  <span class="search"></span><span class="go">Search</span>
</nav>

<section class="abs hero">
  <div class="abs hero-photo" role="img" aria-label="Bouquet of orange lilies, yellow rose and pink gerberas"></div>
  <div class="abs hero-kicker">Some text here</div>
  <div class="abs hero-title">Some text here</div>
  <p class="abs hero-copy">Some text here Some text here Some text here Some text here Some text here Some text here Some text here Some text here Some text here Some text here Some text here Some text here Some text here Some text here Some text here Some text here Some text here Some text here</p>
  <div class="abs btn-shop">Shop now</div>
  <div class="abs dots"><i class="on"></i><i></i><i></i><i></i><i></i><i></i></div>
  <div class="abs arrow" style="left:715px"><svg width="10" height="12"><path d="M7 1 2 6l5 5" stroke="#fff" stroke-width="2.2" fill="none"/></svg></div>
  <div class="abs arrow" style="left:747px"><svg width="10" height="12"><path d="M3 1l5 5-5 5" stroke="#fff" stroke-width="2.2" fill="none"/></svg></div>
</section>

<section class="abs card" style="left:67px;width:253px">
  <h2>Customer favourites and clients testimonials</h2>
  <div class="photo" role="img" aria-label="Group of smiling young customers" style="background:linear-gradient(90deg,#e8c6a4,#c7a58a 50%,#a9b4c2)"></div>
  <p>Stuck on what to choose? Get inspired by our customer favourites. If you have something specific in mind or prefer a Bespoke arrangement or bouquet, contact us for a free consultation.</p>
</section>
<section class="abs card" style="left:342px;width:252px">
  <h2>The Bloom Club</h2>
  <div class="photo" role="img" aria-label="Modern white villa under a blue sky" style="background:linear-gradient(#8fb4d6,#e9e0cf 55%,#7a9a4e)"></div>
  <p>Come and join our community of taste makers where privileges include member specials and newsletter updates on what's hot and happening. Get ideas on selecting the best flowers for your loved one, your home or your wedding. Join today and get free delivery on your first order! It's just our little way of saying thank you!</p>
</section>
<section class="abs card" style="left:618px;width:254px">
  <h2>Our Service Guarantee</h2>
  <div class="photo" role="img" aria-label="Business handshake" style="background:linear-gradient(90deg,#2e2e36,#f4f4f4 40%,#f4f4f4 60%,#2e2e36)"></div>
  <p>At Wrenfield Flowers we are committed to excellence in the design and delivery of our floral services and products. If, for any reason, you are not 100% satisfied please contact us.</p>
</section>

<section class="abs featured">
  <h2>Featured Products</h2>
  <svg class="abs chev" style="left:13px" width="12" height="16"><path d="M10 2 3 8l7 6" stroke="var(--pink-deep)" stroke-width="2.6" fill="none"/></svg>
  <svg class="abs chev" style="left:778px" width="12" height="16"><path d="M2 2l7 6-7 6" stroke="var(--pink-deep)" stroke-width="2.6" fill="none"/></svg>
  <div class="abs prod" style="left:15px"><div class="photo" role="img" aria-label="Pink roses and gerberas in a pink pot" style="background:radial-gradient(#f39bb6,#f7d3de 70%,rgba(255,255,255,0))"></div><div class="price">$<br>25.75</div><div class="name">Flower name put here</div></div>
  <div class="abs sep" style="left:201px"></div>
  <div class="abs prod" style="left:214px"><div class="photo" role="img" aria-label="Yellow lilies and cream roses in a yellow vase" style="background:radial-gradient(#f2dc4e,#f8efb4 70%,rgba(255,255,255,0))"></div><div class="price">$<br>32.5</div><div class="name">Flower name put here</div></div>
  <div class="abs sep" style="left:400px"></div>
  <div class="abs prod" style="left:417px"><div class="photo" role="img" aria-label="Red and orange gerberas in a glass vase" style="background:radial-gradient(#ef4b2e,#f8b7a0 70%,rgba(255,255,255,0))"></div><div class="price">$<br>19.45</div><div class="name">Flower name put here</div></div>
  <div class="abs sep" style="left:600px"></div>
  <div class="abs prod" style="left:615px"><div class="photo" role="img" aria-label="Bright mixed birthday bouquet in pink wrap" style="background:radial-gradient(#f38b3a,#f497c4 70%,rgba(255,255,255,0))"></div><div class="price">$<br>41.40</div><div class="name">Flower name put here</div></div>
</section>

<footer class="abs footer">
  <h3>Get in touch</h3>
  <div class="line" style="top:45px"><svg width="9" height="10"><path d="M2 1h2l1 3-1.5 1a6 6 0 0 0 2.5 2.5L7 6l2 1v2c-4 0-8-4-8-8z" fill="#fff"/></svg>+971500000412</div>
  <div class="line" style="top:63px"><svg width="10" height="8"><rect x=".5" y=".5" width="9" height="7" fill="none" stroke="#fff"/><path d="M.5.5 5 4.5 9.5.5" stroke="#fff" fill="none"/></svg>info@wrenfieldflowers.com</div>
  <div class="line" style="top:86px;gap:5px"><span class="sq"></span><span class="sq"></span><span class="sq"></span></div>
  <div class="vr" style="left:187px"></div>
  <div class="copy">Copyright 2013 www.wrenfield.com<br>All rights reserved.</div>
  <div class="vr" style="left:387px"></div>
  <div class="links">About Us &nbsp;|&nbsp; FAQs &nbsp;|&nbsp; Secure Payment &nbsp;|&nbsp; Policy &nbsp;|&nbsp; Terms and conditions &nbsp;|&nbsp; Contact us</div>
</footer>

</body>
</html>
```